Dentistry

Dentist's personal business card. No logo needed. The card shoul deliver the massage of reliability, professionalism, experience.
Please ad the full brief of the project: down the line it says: the winning look should be precise and pristine NO pictures of Teeth, smiles, instruments etc.

The details to be desplaid are:
Dr. Rob Valdoni
Doctor of Dental Surgery
PHD
Web. Www.drvaldoni.com
Email. Rob@drvaldoni.com
Tel 07731482590
Surgery address. 27Bharwick road London SW4 7QN UK
82 Fenwyn Row London SW3 2HT. Uk

Reason: Decided to make the payment unrefundable in order to get more designers involved.

Requirements
Should not have
• Logo, teeth, smile any sort of instruments.

```html
<!DOCTYPE html>
<html lang="en">
<head>
<meta charset="utf-8">
<title>Dentistry Business Card</title>
<link rel="stylesheet" href="https://fonts.googleapis.com/css2?family=Jost:wght@500&family=Open+Sans:wght@400;600&display=swap">
<style>
  :root {
    --brand-blue: #138fe3;
    --card-white: #ffffff;
    --ink-grey: #555a60;
    --stage: #ebeced;
    --shadow: rgba(0, 0, 0, 0.18);
  }
  * { box-sizing: border-box; margin: 0; padding: 0; }
  html, body {
    width: 1200px;
    height: 800px;
    overflow: hidden;
    background: var(--stage);
  }
  .stage {
    width: 1200px;
    height: 800px;
    display: flex;
    align-items: center;
    justify-content: center;
    gap: 30px;
  }
  .card {
    position: relative;
    width: 560px;
    height: 310px;
    border-radius: 14px;
    overflow: hidden;
    box-shadow: 0 8px 22px var(--shadow);
  }
  /* Front */
  .card--front { background: var(--brand-blue); }
  .name-band {
    position: absolute;
    left: 96px;
    right: 0;
    top: 128px;
    height: 98px;
    background: var(--card-white);
    border-radius: 49px 0 0 49px;
    display: flex;
    align-items: center;
    padding: 0 28px 0 26px;
  }
  .name-band__title {
    font-family: "Jost", sans-serif;
    font-weight: 500;
    font-size: 24px;
    letter-spacing: 0.4px;
    color: var(--brand-blue);
    white-space: nowrap;
  }
  /* Back */
  .card--back { background: var(--card-white); }
  .contact-band {
    position: absolute;
    left: 0;
    top: 100px;
    width: 235px;
    height: 104px;
    background: var(--brand-blue);
    border-radius: 0 52px 52px 0;
    padding: 16px 0 0 26px;
    display: flex;
    flex-direction: column;
    gap: 6px;
  }
  .contact-line {
    display: flex;
    align-items: center;
    gap: 8px;
    font-family: "Open Sans", sans-serif;
    font-size: 13px;
    color: var(--card-white);
    white-space: nowrap;
  }
  .contact-line svg { width: 14px; height: 14px; flex: none; }
  .address-list {
    position: absolute;
    left: 262px;
    top: 133px;
    display: flex;
    flex-direction: column;
    gap: 6px;
  }
  .address-line {
    display: flex;
    align-items: center;
    gap: 8px;
    font-family: "Open Sans", sans-serif;
    font-size: 12px;
    color: var(--ink-grey);
    white-space: nowrap;
  }
  .address-line svg { width: 14px; height: 14px; flex: none; }
  .edge-bar {
    position: absolute;
    right: 0;
    top: 100px;
    width: 18px;
    height: 104px;
    background: var(--brand-blue);
  }
</style>
</head>
<body>
<main class="stage">

  <section class="card card--front" aria-label="Card front">
    <div class="name-band">
      <h1 class="name-band__title">DR. ROB VALDONI / DENTISTRY</h1>
    </div>
  </section>

  <section class="card card--back" aria-label="Card back">
    <div class="contact-band">
      <p class="contact-line">
        <svg viewBox="0 0 16 16" aria-hidden="true"><path fill="#1b1b1b" d="M4.2 1.5l2 3.2-1.3 1.4c.8 1.9 2.2 3.3 4 4.1l1.4-1.3 3.2 2-1 2.6C7.3 13.9 2.1 8.7 1.6 3.6z"/></svg>
        07731482590
      </p>
      <p class="contact-line">
        <svg viewBox="0 0 16 16" aria-hidden="true"><rect x="1.5" y="3.5" width="13" height="9" fill="none" stroke="#1b1b1b" stroke-width="1.4"/><path d="M1.5 3.5L8 9l6.5-5.5" fill="none" stroke="#1b1b1b" stroke-width="1.4"/></svg>
        Rob@drvaldoni.com
      </p>
      <p class="contact-line">
        <svg viewBox="0 0 16 16" aria-hidden="true"><g fill="none" stroke="#1b1b1b" stroke-width="1.2"><circle cx="8" cy="8" r="6.5"/><ellipse cx="8" cy="8" rx="2.8" ry="6.5"/><path d="M1.5 8h13M2.6 4.5h10.8M2.6 11.5h10.8"/></g></svg>
        Www.drvaldoni.com
      </p>
    </div>

    <div class="address-list">
      <p class="address-line">
        <svg viewBox="0 0 16 16" aria-hidden="true"><path fill="#138fe3" d="M8 1.5L1 8h2v6.5h4V10h2v4.5h4V8h2z"/></svg>
        27Bharwick road London SW4 7QN UK
      </p>
      <p class="address-line">
        <svg viewBox="0 0 16 16" aria-hidden="true"><path fill="#138fe3" d="M8 1.5L1 8h2v6.5h4V10h2v4.5h4V8h2z"/></svg>
        82 Fenwyn Row London SW3 2HT. Uk
      </p>
    </div>

    <div class="edge-bar"></div>
  </section>

</main>
</body>
</html>
```